Pamphlet for introducing people to our church

I would like a church pamphlet designed, that includes the content in file "vosti-pamphlet.txt".

I am looking for a design that will incorporate the content in a professional and creative manner.

You do not have to use the content in any specific order, but I am relying on your skill and design knowledge to organize everything in an artistic and effective way.

Target Market(s)

Everyone

Industry/Entity Type

Religious

Requirements
Must have
• logo, use of content provided, use of branding (logo colors)
Nice to have
• More images where necessary
Should not have
• cross

```html
<!DOCTYPE html>
<html lang="en">
<head>
<meta charset="utf-8">
<title>Vosti Pamphlet</title>
<link href="https://fonts.googleapis.com/css2?family=Cinzel:wght@400;600&family=Roboto:ital,wght@0,400;0,500;0,700;1,400&display=swap" rel="stylesheet">
<style>
:root{
  --stage:#dc8418;
  --navy:#1d3f66;
  --navy-deep:#0f3a5f;
  --orange:#f0922a;
  --ink:#464646;
  --paper:#e2ddd8;
  --white:#ffffff;
}
*{margin:0;padding:0;box-sizing:border-box}
html,body{width:1200px;height:984px;overflow:hidden}
body{background:var(--stage);position:relative;font-family:'Roboto',Arial,sans-serif}
.page{position:absolute;top:143px;width:467px;height:661px;overflow:hidden;box-shadow:0 6px 18px rgba(0,0,0,.28)}
.page-front{left:126px;background:#fbf3ea}
.page-back{left:647px;background:var(--paper)}

/* front */
.front-photo{position:absolute;inset:0;background:
  radial-gradient(ellipse at 72% 55%,rgba(185,110,70,.85) 0%,rgba(220,150,100,.55) 30%,rgba(245,215,180,.2) 55%,rgba(255,250,244,0) 70%),
  linear-gradient(100deg,#fffaf3 0%,#fdf0e2 45%,#f1c9a2 75%,#e7b08a 100%)}
.brand{position:absolute;left:32px;top:80px;font-family:'Cinzel',serif;font-size:60px;line-height:56px;color:var(--navy);letter-spacing:2px}
.tagline{position:absolute;left:45px;top:139px;font-family:'Cinzel',serif;font-size:14px;color:var(--orange);letter-spacing:.5px}
.section-title{position:absolute;left:29px;top:175px;font-family:'Cinzel',serif;font-size:19px;color:var(--navy);letter-spacing:.5px}
.mission{position:absolute;left:27px;top:215px;width:206px;font-size:11.4px;line-height:14.7px;color:var(--ink)}
.ministries{position:absolute;left:15px;top:509px;width:433px;height:132px;border-radius:8px;background:rgba(23,72,112,.93);color:var(--white);text-align:center}
.ministries h2{font-family:'Cinzel',serif;font-weight:400;font-size:28px;color:var(--orange);margin-top:12px;line-height:30px}
.ministries .rule{width:252px;height:1px;background:rgba(255,255,255,.7);margin:3px auto 6px}
.ministries h3{font-weight:400;font-size:12.5px;letter-spacing:.2px}
.ministries p{font-size:10.5px;line-height:15px;margin:10px 14px 0}

/* back */
.back-photo{position:absolute;left:0;top:0;width:467px;height:400px;background:
  radial-gradient(ellipse at 40% 35%,rgba(190,170,150,.9) 0%,rgba(120,100,85,.6) 35%,rgba(30,25,22,0) 65%),
  linear-gradient(180deg,#2a2420 0%,#4a3f37 45%,#a59a90 78%,var(--paper) 100%)}
.service{position:absolute;left:25px;top:389px;color:var(--navy)}
.service h2{font-size:20px;font-weight:700;letter-spacing:.3px;display:flex;align-items:center;gap:6px}
.service .time{font-size:15px;margin:6px 0 0 24px}
.venue{position:absolute;left:34px;top:463px;display:flex;gap:9px;color:var(--navy);font-size:15px;line-height:18.5px}
.contact-band{position:absolute;left:0;top:538px;width:467px;height:95px}
.call{position:absolute;left:0;top:0;width:240px;height:95px;background:var(--navy-deep);color:var(--orange);text-align:center}
.call p{font-size:14px;line-height:18px;margin-top:11px}
.call .phone{font-size:25px;font-weight:700;margin-top:6px;line-height:28px}
.online{position:absolute;left:222px;top:0;width:245px;height:95px;text-align:center;color:var(--navy-deep)}
.online svg{position:absolute;inset:0}
.online .label{position:relative;font-style:italic;font-size:13.5px;line-height:16px;display:flex;align-items:center;justify-content:center;gap:4px}
.online .label::before,.online .label::after{content:"";width:18px;height:1px;background:var(--navy-deep)}
.online .value{position:relative;font-weight:700;font-size:14.5px;line-height:18px}
.online .first{margin-top:9px}
.online .second{margin-top:7px}
</style>
</head>
<body>

<section class="page page-front">
  <div class="front-photo" role="img" aria-label="Photo of a smiling child with curly hair looking upward in warm light"></div>
  <div class="brand">VOSTI</div>
  <div class="tagline">Light for Every Nation</div>
  <h2 class="section-title">MISSION STATEMENT</h2>
  <p class="mission">VOSTI is a gathering of believers whose purpose is to seek the face of God for an authentic restoration of the church as a body of born again believers around the world. As a gathering of believers, VOSTI seeks an awakening of the mind founded on the precepts and teachings of Jesus Christ. The modern church has replaced the simple and Kingdom centered principles of Jesus's disciples with complacent and compromised teachings on earthly prosperity. We believe in humbly seeking God without motive to use God or His Word for our own gain. The end times church will experience a glorious revival, renewed love and zeal for true discipleship, faith, and godliness as Jesus intended for us.</p>
  <div class="ministries">
    <h2>MINISTRIES</h2>
    <div class="rule"></div>
    <h3>LITTLE SPROUTS (CHILDREN'S MINISTRY)</h3>
    <p>Children learn to be seeds of godliness in the world. Pathway class: learn the basics of Christian faith and about God's purpose for your life. Deeper class: deepen your knowledge of God's word and learn how to serve him.</p>
  </div>
</section>

<section class="page page-back">
  <div class="back-photo" role="img" aria-label="Photo of folded hands resting on a Bible in prayer"></div>
  <div class="service">
    <h2>
      <svg width="18" height="18" viewBox="0 0 18 18" aria-hidden="true"><circle cx="9" cy="9" r="7.5" fill="none" stroke="currentColor" stroke-width="2"/><path d="M9 5v4.5H6" fill="none" stroke="currentColor" stroke-width="1.8"/></svg>
      SUNDAY SERVICE
    </h2>
    <div class="time">10:00 AM - 12:30 PM</div>
  </div>
  <div class="venue">
    <svg width="14" height="20" viewBox="0 0 14 20" aria-hidden="true"><path d="M7 0C3.1 0 0 3.1 0 7c0 5 7 13 7 13s7-8 7-13c0-3.9-3.1-7-7-7zm0 9.6A2.6 2.6 0 1 1 7 4.4a2.6 2.6 0 0 1 0 5.2z" fill="currentColor"/></svg>
    <address style="font-style:normal">Linden Community Center<br>48 Alder Street<br>Portland, ME 04101</address>
  </div>
  <div class="contact-band">
    <div class="call">
      <p>if you need prayer or<br>counseling give us a call at</p>
      <div class="phone">+1 207-555-0148</div>
    </div>
    <div class="online">
      <svg width="245" height="95" viewBox="0 0 245 95" aria-hidden="true"><path d="M0 95C2 40 10 10 22 0H245V95Z" fill="#e8e8ea"/></svg>
      <div class="label first">Visit us</div>
      <div class="value">www.vosti.org</div>
      <div class="label second">email us</div>
      <div class="value">contact@cedarhall.org</div>
    </div>
  </div>
</section>

</body>
</html>
```